Business Card Design

Our Motto is "Protecting Australia's Underground Utilities"

We want the Southern Cross inside a shield I have attached the southern cross and our old shield design

Product description is: Vacuum Excavation & Utility Location
Wet & Dry Vacuum Loading
Confined Space Entry Specialists
High Pressure Cleaning

The Southern Cross in the shield must be blue and white. The Company name must be Coastal Pipeguard Services. The Green & Gold Shield logo I uploaded is my OLD logo design. Thank you

Target Market(s)

Civil Construction

Industry/Entity Type

Business

Contact Information for Business Card

Coastal Pipeguard Services Pty Ltd
Corey Halbrook(Director)
0413862975
coreyh@pipeguardco.com.au
A.B.N.52938470116

Colors
0456a3

Requirements
Must have
• Southern Cross inside a shield, Blue and white design on the Southern Cross shield.
Must say Coastal Pipeguard Services P/L

```html
<!DOCTYPE html>
<html lang="en">
<head>
<meta charset="utf-8">
<title>Coastal Pipeguard Services – Business Card</title>
<link rel="stylesheet" href="https://fonts.googleapis.com/css2?family=Arimo:wght@400;700&family=Open+Sans:wght@400;600&display=swap">
<style>
  :root {
    --brand-blue: #0456a3;
    --card-white: #ffffff;
    --backdrop: #eceef1;
    --text-light: #ffffff;
    --shadow: rgba(0, 0, 0, 0.18);
  }
  * { box-sizing: border-box; margin: 0; padding: 0; }
  html, body {
    width: 1200px;
    height: 800px;
    overflow: hidden;
    background: var(--backdrop);
  }
  .stage {
    position: relative;
    width: 1200px;
    height: 800px;
  }
  .card {
    position: absolute;
    width: 540px;
    height: 310px;
    overflow: hidden;
    box-shadow: 0 6px 18px var(--shadow);
  }

  /* Reverse side */
  .card-back {
    left: 90px;
    top: 80px;
    background: var(--brand-blue);
    color: var(--text-light);
    font-family: "Open Sans", sans-serif;
    text-align: center;
  }
  .card-back .motto {
    margin-top: 48px;
    font-size: 17px;
    font-weight: 400;
    letter-spacing: 0.3px;
  }
  .card-back .services {
    list-style: none;
    margin-top: 16px;
    font-size: 13px;
    line-height: 18px;
    letter-spacing: 0.3px;
  }
  .card-back .brand {
    margin-top: 26px;
    display: flex;
    flex-direction: column;
    align-items: center;
    gap: 8px;
  }
  .card-back .brand-dot {
    width: 46px;
    height: 46px;
    border-radius: 50%;
    background: var(--card-white);
  }
  .card-back .brand-name {
    font-size: 10px;
    font-weight: 600;
  }

  /* Front side */
  .card-front {
    left: 570px;
    top: 410px;
    background: var(--card-white);
    font-family: "Arimo", sans-serif;
  }
  .card-front .sweep {
    position: absolute;
    inset: 0;
  }
  .card-front .brand {
    position: absolute;
    left: 40px;
    top: 70px;
    width: 220px;
    display: flex;
    flex-direction: column;
    align-items: center;
    gap: 14px;
  }
  .card-front .brand-dot {
    width: 90px;
    height: 90px;
    border-radius: 50%;
    background: var(--brand-blue);
  }
  .card-front .brand-name {
    color: var(--brand-blue);
    font-size: 15px;
    font-weight: 700;
  }
  .card-front .contact {
    position: absolute;
    right: 30px;
    top: 150px;
    color: var(--text-light);
    text-align: right;
  }
  .card-front .person-name {
    font-size: 18px;
    font-weight: 400;
    letter-spacing: 0.4px;
  }
  .card-front .person-role {
    font-size: 12px;
    margin-bottom: 12px;
  }
  .card-front .details {
    list-style: none;
    font-size: 13px;
    line-height: 18px;
  }
  .card-front .details li {
    display: flex;
    justify-content: flex-end;
    align-items: center;
    gap: 8px;
  }
  .card-front .details svg {
    width: 14px;
    height: 14px;
    flex: none;
  }
  .card-front .details .no-icon { padding-right: 22px; }
</style>
</head>
<body>
<main class="stage">

  <section class="card card-back" aria-label="Business card reverse">
    <p class="motto">Protecting Australia's Underground Utilities</p>
    <ul class="services">
      <li>Vacuum Excavation &amp; Utility Location</li>
      <li>Wet &amp; Dry Vacuum Loading</li>
      <li>Confined Space Entry Specialists</li>
      <li>High Pressure Cleaning</li>
    </ul>
    <div class="brand">
      <span class="brand-dot"></span>
      <span class="brand-name">Coastal Pipeguard Services</span>
    </div>
  </section>

  <section class="card card-front" aria-label="Business card front">
    <svg class="sweep" viewBox="0 0 540 310" preserveAspectRatio="none" aria-hidden="true">
      <path d="M300 0 C365 60 375 205 165 310 L540 310 L540 0 Z" fill="var(--brand-blue)"/>
      <path d="M314 0 C378 70 382 215 196 310" fill="none" stroke="var(--card-white)" stroke-width="3"/>
    </svg>

    <div class="brand">
      <span class="brand-dot"></span>
      <span class="brand-name">Coastal Pipeguard Services</span>
    </div>

    <div class="contact">
      <p class="person-name">Corey Halbrook</p>
      <p class="person-role">Director</p>
      <ul class="details">
        <li>0413862975
          <svg viewBox="0 0 16 16" aria-hidden="true"><path d="M3 2h3l1.5 3.5-2 1.2a8 8 0 0 0 3.8 3.8l1.2-2L14 10v3a1 1 0 0 1-1 1A11 11 0 0 1 2 3a1 1 0 0 1 1-1z" fill="var(--text-light)"/></svg>
        </li>
        <li>coreyh@pipeguardco.com.au
          <svg viewBox="0 0 16 16" aria-hidden="true"><rect x="1.5" y="3.5" width="13" height="9" fill="none" stroke="var(--text-light)" stroke-width="1.4"/><path d="M1.5 3.5 8 9l6.5-5.5" fill="none" stroke="var(--text-light)" stroke-width="1.4"/></svg>
        </li>
        <li>www.pipeguardco.com.au
          <svg viewBox="0 0 16 16" aria-hidden="true"><rect x="1.5" y="2.5" width="13" height="9" fill="none" stroke="var(--text-light)" stroke-width="1.4"/><path d="M5 14h6M8 11.5V14" stroke="var(--text-light)" stroke-width="1.4"/></svg>
        </li>
        <li class="no-icon">A.B.N.52938470116</li>
      </ul>
    </div>
  </section>

</main>
</body>
</html>
```